Velvet Fern Beauty Bar Business Card

We need a modern, elegant business card design for our new beauty bar located in La Quinta, CA. The card should feel premium yet approachable, reflecting our brand identity: warm, stylish, and confidence-boosting.

Use our existing Velvet Fern Beauty Bar logo (to be provided as vector file).

Colors: Black, White, Blush / Nude accents, and Gold (metallic or foil effect if possible).

Typography: Clean sans-serif for clarity, with optional elegant script accent.
Design Style

Minimalist and modern with plenty of white space.

Premium look with a beauty/lifestyle feel (not overly corporate).

Option to explore vertical or horizontal orientation.

Rounded corners welcome, but not required.

Additional Notes

Design should print well in both matte and glossy finishes.

Please present mockups with both light and dark backgrounds.

Keep overall feel sleek, feminine, and high-end while still being approachable.

```html
<!DOCTYPE html>
<html lang="en">
<head>
<meta charset="utf-8">
<title>Velvet Fern Beauty Bar – Business Card</title>
<link href="https://fonts.googleapis.com/css2?family=Lato:wght@400;700&display=swap" rel="stylesheet">
<style>
  :root {
    --backdrop: #2e2e2e;
    --card: #050505;
    --gold: #c9a45a;
    --gold-light: #f0d89a;
    --gold-dark: #8a6a2c;
    --white: #ffffff;
  }
  html, body {
    margin: 0;
    width: 1200px;
    height: 900px;
    overflow: hidden;
    background: var(--backdrop);
    font-family: "Lato", sans-serif;
  }
  .canvas {
    position: relative;
    width: 1200px;
    height: 900px;
  }
  .card {
    position: absolute;
    top: 302px;
    width: 513px;
    height: 295px;
    border-radius: 22px;
    background: var(--card);
    overflow: hidden;
    box-shadow: 0 6px 18px rgba(0,0,0,0.55);
  }
  .card--front { left: 73px; }
  .card--back { left: 616px; }

  .brand-name {
    color: var(--gold);
    font-weight: 700;
    margin: 0;
    white-space: nowrap;
  }
  .card--front .brand-name {
    position: absolute;
    left: 0; right: 0;
    top: 130px;
    text-align: center;
    font-size: 34px;
    letter-spacing: 0.5px;
  }
  .card--front .brand-sub {
    position: absolute;
    left: 0; right: 0;
    top: 176px;
    text-align: center;
    color: var(--gold);
    font-size: 16px;
    font-weight: 700;
    margin: 0;
  }

  .holder {
    position: absolute;
    left: 46px;
    top: 38px;
    color: var(--white);
  }
  .holder-name { margin: 0; font-size: 15px; font-weight: 700; letter-spacing: 0.3px; }
  .holder-role { margin: 3px 0 0; font-size: 9px; font-weight: 700; letter-spacing: 0.3px; }

  .address {
    position: absolute;
    left: 46px;
    top: 162px;
    margin: 0;
    color: var(--white);
    font-size: 13px;
    line-height: 17px;
    font-style: normal;
  }
  .contacts {
    position: absolute;
    left: 46px;
    top: 230px;
    margin: 0;
    padding: 0;
    list-style: none;
    color: var(--white);
    font-size: 14.5px;
    line-height: 20px;
  }
  .contacts li { display: flex; align-items: center; gap: 10px; }
  .contacts svg { width: 11px; height: 11px; fill: var(--gold); }

  .swoosh { position: absolute; left: 0; top: 0; }

  .profile-art {
    position: absolute;
    right: 0;
    top: 28px;
    width: 225px;
    height: 267px;
    background: radial-gradient(ellipse at 70% 40%, rgba(201,164,90,0.45), rgba(138,106,44,0.2) 55%, rgba(5,5,5,0) 80%);
  }
  .card--back .brand-lockup {
    position: absolute;
    right: 22px;
    top: 238px;
    text-align: center;
  }
  .card--back .brand-name { font-size: 15px; }
  .card--back .brand-sub { margin: 1px 0 0; color: var(--gold); font-size: 9px; font-weight: 700; }
</style>
</head>
<body>
<main class="canvas">
  <section class="card card--front">
    <p class="brand-name">Velvet Fern Beauty Bar</p>
    <p class="brand-sub">— by Marisol —</p>
  </section>

  <section class="card card--back">
    <svg class="swoosh" width="513" height="295" viewBox="0 0 513 295" aria-hidden="true">
      <defs>
        <linearGradient id="goldSweep" x1="0" x2="1" y1="0" y2="0">
          <stop offset="0" stop-color="#8a6a2c"/>
          <stop offset="0.5" stop-color="#f0d89a"/>
          <stop offset="1" stop-color="#c9a45a"/>
        </linearGradient>
      </defs>
      <path d="M0 240 C 60 212, 150 200, 300 212 C 250 205, 110 210, 0 234 Z" fill="url(#goldSweep)"/>
      <path d="M300 212 C 330 215, 350 220, 360 223" stroke="#c9a45a" stroke-width="1" fill="none"/>
    </svg>

    <div class="holder">
      <p class="holder-name">OWEN CALLOWAY</p>
      <p class="holder-role">MANAGING DIRECTOR</p>
    </div>

    <address class="address">48 Placid Lane<br>Fairview, New York 10234</address>

    <ul class="contacts">
      <li><svg viewBox="0 0 24 24"><path d="M6.6 10.8a15 15 0 0 0 6.6 6.6l2.2-2.2a1 1 0 0 1 1-.25 11.4 11.4 0 0 0 3.6.57 1 1 0 0 1 1 1V20a1 1 0 0 1-1 1A17 17 0 0 1 3 4a1 1 0 0 1 1-1h3.5a1 1 0 0 1 1 1c0 1.25.2 2.45.57 3.57a1 1 0 0 1-.25 1z"/></svg>555 210 48 73</li>
      <li><svg viewBox="0 0 24 24"><path d="M2 5h20v14H2z M2 5l10 8 10-8" /></svg>info@velvetfern.com</li>
      <li><svg viewBox="0 0 24 24"><circle cx="12" cy="12" r="10"/></svg>www.velvetfern.com</li>
    </ul>

    <div class="profile-art" role="img" aria-label="Gold line illustration of a woman's profile"></div>

    <div class="brand-lockup">
      <p class="brand-name">Velvet Fern Beauty Bar</p>
      <p class="brand-sub">— by Marisol —</p>
    </div>
  </section>
</main>
</body>
</html>
```